Harborline Talent IT Recruiting firm needs a business card design for Recruiters, Sourcers, and Account

We need business cards that allow us to change all contact info, names, titles (Recruiter, Sourcer, Account Manager, Director, CEO, etc) per person since we have three offices, in three cities, Phoenix, Austin, and Las Vegas. We do recruiting and contractors for IT positions (Developers, Architects, Software Engineers, Security Engineers, Help Desk, DBAs, PMs, Scrum Masters, etc.) Our client companies are very diverse from Crestline 250 to silicone Valley type start-ups.

So, while we what hip, techie, and quirky, it still needs to be professional. Primary color we use is blue, with silver as a secondary color.

Target Market(s)

IT, Technology

Industry/Entity Type

Business

Contact Information for Business Card

Company name: Harborline Talent, Inc.
Website: www.harborlinetalent-example.com
Logos for ProCircle, Quillo, and Roomwall

Name, Title, Office Number, Cell Number, email

Font styles to use
Serif
Sans Serif

Colors
0455a3
d5d5d5

Requirements
Nice to have
• The grey I selected below is not necessary - but, would like silver included. I included a card design (File 3: HTI early trial example.jpg) that I had started on. It's very rough, and not quite what we're looking for, but what we did like is the logo, big, maybe a bit faded, off center, goes out of frame, etc. Still looking for other ideas - you are the pros! But, just an idea of a design element we liked.

```html
<!DOCTYPE html>
<html lang="en">
<head>
<meta charset="utf-8">
<title>Harborline Talent Business Card</title>
<link rel="stylesheet" href="https://fonts.googleapis.com/css2?family=Cinzel:wght@400;600&family=Ubuntu:wght@400;700&display=swap">
<style>
  :root {
    --brand-blue: #0455a3;
    --brand-blue-light: #0a7fc0;
    --brand-blue-deep: #0b3f7e;
    --silver: #d5d5d5;
    --card-white: #f7f7f7;
    --ink: #1e1e1e;
    --page-bg: #2a2a2a;
  }
  * { box-sizing: border-box; margin: 0; padding: 0; }
  html, body {
    width: 1200px; height: 1000px; overflow: hidden;
    background: var(--page-bg);
  }
  .sheet {
    width: 1200px; height: 1000px;
    display: flex; flex-direction: column; align-items: center; justify-content: center;
    gap: 40px;
  }
  .card {
    position: relative; width: 700px; height: 400px; overflow: hidden;
  }

  /* Front */
  .card-front {
    background: linear-gradient(135deg, #ffffff 0%, var(--card-white) 55%, var(--silver) 100%);
  }
  .emblem-area {
    position: absolute; left: -190px; top: 40px;
    width: 560px; height: 560px; border-radius: 50%;
    background: linear-gradient(160deg, var(--brand-blue-light) 0%, var(--brand-blue) 55%, var(--brand-blue-deep) 100%);
  }
  .front-wordmark {
    position: absolute; left: 10px; top: 300px; width: 350px; text-align: center;
    color: #ffffff; font-family: "Cinzel", serif;
  }
  .front-wordmark .company-name {
    font-size: 26px; font-weight: 600; letter-spacing: 0.5px; white-space: nowrap;
  }
  .front-wordmark .tagline {
    font-size: 13px; letter-spacing: 1.5px; margin-top: 2px; white-space: nowrap;
  }
  .contact-block {
    position: absolute; left: 388px; top: 82px;
    font-family: "Ubuntu", sans-serif; color: var(--ink);
    white-space: nowrap;
  }
  .person-name { color: var(--brand-blue); font-weight: 700; font-size: 21px; }
  .person-title { color: var(--brand-blue); font-size: 16px; margin-top: 4px; }
  .social-list { list-style: none; margin-top: 34px; font-size: 15px; }
  .social-list li { display: flex; align-items: center; gap: 8px; height: 22px; }
  .social-dot { width: 15px; height: 15px; border-radius: 50%; background: var(--brand-blue-light); }
  .contact-lines { list-style: none; margin-top: 28px; font-size: 14px; line-height: 24px; }

  /* Back */
  .card-back {
    background: linear-gradient(200deg, var(--brand-blue-light) 0%, var(--brand-blue) 50%, var(--brand-blue-deep) 100%);
    color: #ffffff; font-family: "Cinzel", serif;
  }
  .back-wordmark { position: absolute; left: 120px; top: 110px; width: 460px; text-align: right; }
  .back-wordmark .line-one { font-size: 62px; font-weight: 600; line-height: 1; letter-spacing: 1px; }
  .back-wordmark .line-two { font-size: 50px; font-weight: 600; line-height: 1.1; letter-spacing: 3px; }
  .back-tagline {
    position: absolute; left: 120px; top: 272px; width: 460px; text-align: center;
    font-size: 20px; letter-spacing: 2.5px; color: rgba(255,255,255,0.85);
  }
</style>
</head>
<body>
<main class="sheet">
  <section class="card card-front">
    <div class="emblem-area" role="img" aria-label="Large brand emblem area in blue, bleeding off the card edge"></div>
    <div class="front-wordmark">
      <div class="company-name">HARBORLINE TALENT</div>
      <div class="tagline">CHARTING THE COURSE</div>
    </div>
    <div class="contact-block">
      <div class="person-name">Jordan Wells</div>
      <div class="person-title">First Touch Embassador</div>
      <ul class="social-list">
        <li><span class="social-dot"></span>@JordanWellsHT</li>
        <li><span class="social-dot"></span>ProCircle</li>
      </ul>
      <ul class="contact-lines">
        <li>p : 555.014.2738</li>
        <li>e : jordan@harborlinetalent-example.com</li>
        <li>w : www.harborlinetalent-example.com</li>
      </ul>
    </div>
  </section>

  <section class="card card-back">
    <div class="back-wordmark">
      <div class="line-one">HARBORLINE</div>
      <div class="line-two">TALENT</div>
    </div>
    <div class="back-tagline">CHARTING THE COURSE</div>
  </section>
</main>
</body>
</html>
```